Professional Package for CPA Firm

We would like a stationery design for our new CPA Firm based in Atlanta, GA called 'Vale 7'. We work with investors to help grow investments, tax free. We would like the design to have a professional/minimal look with a 'wow' factor. We need 9.5″ x 4.125″, 9x12, and 10x13 mailing envelopes, business cards, and a letterhead. We have a logo that is already complete. For the letterhead, we would like to have space to put credentials at the bottom of the page

Industry/Entity Type

CPA, Accounting

```html
<!DOCTYPE html>
<html lang="en">
<head>
<meta charset="utf-8">
<title>Vale 7 Stationery</title>
<link href="https://fonts.googleapis.com/css2?family=Montserrat:wght@400;700;800&family=Open+Sans:wght@400;600;700&display=swap" rel="stylesheet">
<style>
  :root {
    --blue: #1fa3dc;
    --blue-deep: #1a8dcb;
    --ink: #111111;
    --text: #5a5a5a;
    --paper: #ffffff;
    --backdrop: #e9e9ea;
    --pale: #cde9f7;
    --line: #d8d8d8;
  }
  * { box-sizing: border-box; margin: 0; padding: 0; }
  html, body { width: 879px; height: 1200px; overflow: hidden; }
  body {
    background: var(--backdrop);
    font-family: "Open Sans", Arial, sans-serif;
    color: var(--text);
    position: relative;
  }
  .sheet { position: absolute; background: var(--paper); box-shadow: 0 2px 6px rgba(0,0,0,.12); overflow: hidden; }

  /* brand name block */
  .brand { display: inline-flex; flex-direction: column; line-height: 1; }
  .brand-name { font-family: "Montserrat", Arial, sans-serif; font-weight: 800; color: var(--ink); letter-spacing: .5px; }
  .brand-tag { font-family: "Montserrat", Arial, sans-serif; font-weight: 400; color: var(--ink); letter-spacing: .4px; margin-top: 3px; }
  .brand.on-blue .brand-name, .brand.on-blue .brand-tag { color: var(--paper); }
  .brand.pale .brand-name, .brand.pale .brand-tag { color: var(--pale); }

  .base-band { position: absolute; left: 0; right: 0; bottom: 0; height: 5px; background: var(--blue); }
  .base-band::before { content: ""; position: absolute; left: 0; top: 0; bottom: 0; width: 8%; background: var(--ink); }

  .icon { width: 7px; height: 7px; fill: var(--blue); flex: none; }
  .contact-line { display: flex; align-items: center; gap: 4px; }

  /* letterhead */
  .letterhead { left: 40px; top: 40px; width: 420px; height: 543px; padding: 36px 36px 0 38px; }
  .letterhead .brand-name { font-size: 19px; }
  .letterhead .brand-tag { font-size: 4.5px; }
  .letterhead-head { display: flex; justify-content: space-between; align-items: flex-start; }
  .letterhead-contact { font-size: 6.5px; line-height: 1.55; color: var(--text); }
  .letter-body { margin-top: 36px; font-size: 6.3px; line-height: 1.55; color: var(--text); text-align: justify; }
  .letter-body p { margin-bottom: 7px; }
  .signature { width: 48px; height: 28px; background: linear-gradient(135deg, #eeeeee, #d9d9d9); margin-top: 8px; }

  /* business cards */
  .card { width: 340px; height: 195px; left: 500px; }
  .card-front { top: 40px; display: flex; align-items: center; padding: 0 24px 10px; }
  .card-front .brand-name { font-size: 20px; }
  .card-front .brand-tag { font-size: 5px; }
  .card-divider { width: 1px; height: 78px; background: var(--ink); margin: 0 16px 0 18px; }
  .card-details { font-size: 6.4px; line-height: 1.6; }
  .card-person { font-family: "Montserrat", Arial, sans-serif; font-weight: 700; font-size: 8.5px; color: var(--ink); line-height: 1.1; }
  .card-role { font-size: 6.4px; color: var(--blue); margin-bottom: 6px; }
  .card-back { top: 255px; background: var(--blue); display: flex; align-items: center; justify-content: center; }
  .card-back .brand { align-items: center; }
  .card-back .brand-name { font-size: 30px; }
  .card-back .brand-tag { font-size: 7px; }

  /* envelopes */
  .envelope { left: 500px; width: 340px; height: 148px; }
  .envelope-flap { top: 470px; }
  .flap { position: absolute; left: 0; top: 0; right: 0; height: 50px; background: var(--blue); border-radius: 0 0 22px 22px; display: flex; justify-content: center; align-items: center; }
  .flap .brand { align-items: center; }
  .flap .brand-name { font-size: 13px; }
  .flap .brand-tag { font-size: 3.5px; }
  .envelope-site { position: absolute; left: 0; right: 0; bottom: 18px; text-align: center; font-size: 5px; color: #888; }
  .envelope-front { top: 636px; padding: 18px 20px; }
  .envelope-front .brand-name { font-size: 13px; }
  .envelope-front .brand-tag { font-size: 3.5px; }
  .return-address { position: absolute; left: 20px; bottom: 16px; font-size: 5px; line-height: 1.4; color: var(--text); }
  .return-address strong { color: var(--blue); font-weight: 400; }

  /* folder */
  .folder { left: 40px; top: 620px; width: 420px; height: 540px; background: var(--blue); display: flex; align-items: center; justify-content: center; }
  .folder .brand { align-items: center; }
  .folder .brand-name { font-size: 52px; }
  .folder .brand-tag { font-size: 11px; margin-top: 8px; letter-spacing: 2px; }
  .folder-site { position: absolute; left: 0; right: 0; bottom: 36px; text-align: center; color: var(--paper); font-size: 10px; }

  /* notebook */
  .notebook { left: 545px; top: 810px; width: 250px; height: 350px; background: var(--blue-deep); border-radius: 2px 10px 10px 2px; display: flex; align-items: center; justify-content: center; }
  .notebook::before { content: ""; position: absolute; left: 0; top: 0; bottom: 0; width: 8px; background: rgba(0,0,0,.12); }
  .notebook .brand { align-items: center; }
  .notebook .brand-name { font-size: 30px; }
  .notebook .brand-tag { font-size: 6.5px; margin-top: 5px; letter-spacing: 1px; }
  .notebook-site { position: absolute; left: 0; right: 0; bottom: 22px; text-align: center; color: var(--paper); font-size: 5px; }
</style>
</head>
<body>

  <svg width="0" height="0" style="position:absolute" aria-hidden="true">
    <defs>
      <symbol id="ico-phone" viewBox="0 0 24 24"><path d="M6.6 10.8a15 15 0 0 0 6.6 6.6l2.2-2.2a1 1 0 0 1 1-.25 11.4 11.4 0 0 0 3.6.57 1 1 0 0 1 1 1V20a1 1 0 0 1-1 1A17 17 0 0 1 3 4a1 1 0 0 1 1-1h3.5a1 1 0 0 1 1 1c0 1.25.2 2.45.57 3.57a1 1 0 0 1-.25 1z"/></symbol>
      <symbol id="ico-mail" viewBox="0 0 24 24"><path d="M2 5h20v14H2z M2 5l10 8 10-8" /></symbol>
      <symbol id="ico-web" viewBox="0 0 24 24"><path d="M12 2a10 10 0 1 0 0 20 10 10 0 0 0 0-20zm0 2c1.3 1.4 2.2 3.6 2.4 7H9.6C9.8 7.6 10.7 5.4 12 4zM4.1 13h3.5c.1 2.3.6 4.3 1.4 5.8A8 8 0 0 1 4.1 13zm0-2A8 8 0 0 1 9 5.2c-.8 1.5-1.3 3.5-1.4 5.8zm5.5 2h4.8c-.2 3.4-1.1 5.6-2.4 7-1.3-1.4-2.2-3.6-2.4-7zm6.8 0h3.5a8 8 0 0 1-4.9 5.8c.8-1.5 1.3-3.5 1.4-5.8zm0-2c-.1-2.3-.6-4.3-1.4-5.8a8 8 0 0 1 4.9 5.8z"/></symbol>
    </defs>
  </svg>

  <!-- letterhead -->
  <section class="sheet letterhead">
    <header class="letterhead-head">
      <div class="brand">
        <span class="brand-name">VALE 7</span>
        <span class="brand-tag">CPAs and Tax Advisors</span>
      </div>
      <div class="letterhead-contact">
        <div>48 Birch Hollow Road,</div>
        <div>Decatur, GA 30030</div>
        <div class="contact-line"><svg class="icon"><use href="#ico-phone"/></svg>+14045550182</div>
        <div class="contact-line"><svg class="icon"><use href="#ico-mail"/></svg>info@valeseven.com</div>
        <div class="contact-line"><svg class="icon"><use href="#ico-web"/></svg>www.valeseven.com</div>
      </div>
    </header>
    <div class="letter-body">
      <p>Dear customer,</p>
      <p>Lorem ipsum dolor sit amet, consectetur adipisicing elit, sed do eiusmod tempor incididunt ut labore et dolore magna aliqua. Ut enim ad minim veniam, quis nostrud exercitation ullamco laboris nisi ut aliquip ex ea commodo consequat. Duis aute irure dolor in reprehenderit in voluptate velit esse cillum dolore eu fugiat nulla pariatur. Excepteur sint occaecat cupidatat non proident, sunt in culpa qui officia deserunt mollit anim id est laborum.</p>
      <p>Lorem ipsum dolor sit amet, consectetur adipisicing elit, sed do eiusmod tempor incididunt ut labore et dolore magna aliqua. Ut enim ad minim veniam, quis nostrud exercitation ullamco laboris nisi ut aliquip ex ea commodo consequat. Duis aute irure dolor in reprehenderit in voluptate velit esse cillum dolore eu fugiat nulla pariatur. Excepteur sint occaecat cupidatat non proident, sunt in culpa qui officia deserunt mollit anim id est laborum.</p>
      <p>Lorem ipsum dolor sit amet, consectetur adipisicing elit, sed do eiusmod tempor incididunt ut labore et dolore magna aliqua. Ut enim ad minim veniam, quis nostrud exercitation ullamco laboris nisi ut aliquip ex ea commodo consequat. Duis aute irure dolor in reprehenderit in voluptate velit esse cillum dolore eu fugiat nulla pariatur. Excepteur sint occaecat cupidatat non proident, sunt in culpa qui officia deserunt mollit anim id est laborum.</p>
      <p>Lorem ipsum dolor sit amet, consectetur adipisicing elit, sed do eiusmod tempor incididunt ut labore et dolore magna aliqua. Ut enim ad minim veniam, quis nostrud exercitation ullamco laboris nisi ut aliquip ex ea commodo consequat. Duis aute irure dolor in reprehenderit.</p>
      <p>Yours Sincerely,</p>
      <div class="signature" role="img" aria-label="Handwritten signature"></div>
    </div>
    <div class="base-band"></div>
  </section>

  <!-- business card front -->
  <section class="sheet card card-front">
    <div class="brand">
      <span class="brand-name">VALE 7</span>
      <span class="brand-tag">CPAs and Tax Advisors</span>
    </div>
    <div class="card-divider"></div>
    <div class="card-details">
      <div class="card-person">DANIEL MARLOWE</div>
      <div class="card-role">Managing Director</div>
      <div>48 Birch Hollow Road,</div>
      <div>Decatur, GA 30030</div>
      <div class="contact-line"><svg class="icon"><use href="#ico-phone"/></svg>+14045550182</div>
      <div class="contact-line"><svg class="icon"><use href="#ico-mail"/></svg>info@valeseven.com</div>
      <div class="contact-line"><svg class="icon"><use href="#ico-web"/></svg>www.valeseven.com</div>
    </div>
    <div class="base-band"></div>
  </section>

  <!-- business card back -->
  <section class="sheet card card-back">
    <div class="brand pale">
      <span class="brand-name">VALE 7</span>
      <span class="brand-tag">CPAs and Tax Advisors</span>
    </div>
  </section>

  <!-- envelope with flap -->
  <section class="sheet envelope envelope-flap">
    <div class="flap">
      <div class="brand on-blue">
        <span class="brand-name">VALE 7</span>
        <span class="brand-tag">CPAs and Tax Advisors</span>
      </div>
    </div>
    <div class="envelope-site">www.websitename.com</div>
  </section>

  <!-- envelope front -->
  <section class="sheet envelope envelope-front">
    <div class="brand">
      <span class="brand-name">VALE 7</span>
      <span class="brand-tag">CPAs and Tax Advisors</span>
    </div>
    <div class="return-address">
      <strong>Vale 7 CPAs and Tax Advisors</strong><br>
      48 Birch Hollow Road,<br>
      Decatur, GA 30030
    </div>
    <div class="base-band"></div>
  </section>

  <!-- presentation folder -->
  <section class="sheet folder">
    <div class="brand on-blue">
      <span class="brand-name">VALE 7</span>
      <span class="brand-tag">CPAs and Tax Advisors</span>
    </div>
    <div class="folder-site">www.valeseven.com</div>
  </section>

  <!-- notebook cover -->
  <section class="sheet notebook">
    <div class="brand on-blue">
      <span class="brand-name">VALE 7</span>
      <span class="brand-tag">CPAs and Tax Advisors</span>
    </div>
    <div class="notebook-site">www.valeseven.com</div>
  </section>

</body>
</html>
```